International Dental Education Website

This project is for a small teaching center on endodontic and micro dentistry in Norway. We need a Wordpress website design to display and highlight dental educational courses. Please use our new logo - see attached file. We like lighter, pastel oriented colors. The following sites are nicely laid out and you can use these as a guideline of sorts but I do want a unique site.
http://vorplex.example/en, http://www.toothmarlow.example/Education.aspx?currentSection=courses&cid=14,
http://www.pulpvesker.example/.
Please create a space for a possible video on the home page. Please include a small contact form on the home page(name, email, phone, text box). Would like a horizonatal naviagtion bar. Would like an image to go across the whole top part of the site and this may rotate. Please use a stock image that shows a classroom type setting. Put phone number at the top of the screen. Put address and sitemap in a footer.

Reason: Upcoming vacation with limited internet access. Please continue to submit any designs. Thanks you.

Reason: The client is from a foreign country and is on an extended vacation.

Target Market(s)

General dentists (GPs) and specialists in Endodontics

Industry/Entity Type

Dental

Requirements
Must have
• Sitemap: HOME, COURSES, LECTURER, CONTACT US,
NORWEGIAN/ENGLISH. Phone number is: +47 93516270. Business name and address: Kali Rom AS, Endodontic Teaching Center,
Fjeldstads vei 17C, 0371 Oslo, Norway.

```html
<!DOCTYPE html>
<html lang="en">
<head>
<meta charset="utf-8">
<title>Kali Rom – Endodontic Teaching Center</title>
<link rel="stylesheet" href="https://fonts.googleapis.com/css2?family=Arimo:wght@400;700&family=Roboto+Condensed:wght@400;700&display=swap">
<style>
:root{
  --teal:#86dbe2;
  --teal-light:#c4eef1;
  --teal-dark:#5cc4cd;
  --panel:#ececec;
  --panel-line:#d6d6d6;
  --row-line:#dadada;
  --field:#dcdcdc;
  --footer:#dcdcdc;
  --text:#555;
  --heading:#2e3a3d;
  --nav-text:#4a4a4a;
  --white:#fff;
}
*{box-sizing:border-box;margin:0;padding:0}
html,body{width:1200px;height:1133px;overflow:hidden;background:var(--white)}
body{position:relative;font-family:"Arimo",Arial,sans-serif;color:var(--text);font-size:14px}
.abs{position:absolute}

/* header */
.topbar{left:29px;top:0;width:1142px;height:46px;background:linear-gradient(#fafafa,#e4e4e4);border-bottom:1px solid #cfcfcf}
.nav{left:223px;top:0;display:flex;height:46px}
.nav a{display:block;height:46px;line-height:48px;padding:0 18px;font-family:"Roboto Condensed",sans-serif;font-size:17px;color:var(--nav-text);text-decoration:none;border-right:1px solid #cfcfcf;background:linear-gradient(#f8f8f8,#e6e6e6)}
.nav a.active{background:linear-gradient(var(--teal-light),var(--teal));color:#1f3a3d}
.contact-top{right:32px;top:13px;display:flex;gap:16px;font-family:"Roboto Condensed",sans-serif;font-weight:700;font-size:15.5px;color:#333;align-items:center;white-space:nowrap}
.contact-top span{display:flex;align-items:center;gap:7px}
.brand{left:46px;top:0;width:145px;height:89px;background:linear-gradient(#fafafa,#e0e0e0);border:1px solid #cfcfcf;border-top:none;border-radius:0 0 6px 6px;box-shadow:0 2px 4px rgba(0,0,0,.15);display:flex;align-items:center;justify-content:center;gap:7px;font-family:"Roboto Condensed",sans-serif;font-weight:700;font-size:25px;color:var(--teal-dark)}
.brand i{width:10px;height:10px;background:var(--teal-dark);border-radius:50%}

/* slider */
.slider{left:29px;top:64px;width:874px;height:418px;background:var(--panel);border:1px solid var(--panel-line);border-radius:3px}
.slide-photo{position:absolute;left:6px;top:6px;width:862px;height:404px;background:linear-gradient(160deg,#b9b3a6 0%,#8a8277 35%,#5d5c5f 65%,#4a4848 100%)}
.arrow{position:absolute;top:150px}
.dots{position:absolute;left:398px;top:385px;display:flex;gap:6px}
.dots i{width:14px;height:14px;border-radius:50%;background:var(--white)}
.dots i.on{background:var(--teal)}

/* side boxes */
.side{left:920px;width:251px;background:var(--panel);border:1px solid var(--panel-line)}
.side h3{height:41px;line-height:41px;padding-left:15px;background:linear-gradient(var(--teal-light),var(--teal));font-family:"Roboto Condensed",sans-serif;font-weight:700;font-size:18px;color:var(--heading)}
.side ul{list-style:none}
.side li{height:33px;line-height:33px;padding-left:30px;border-bottom:1px solid var(--row-line);font-size:13.5px;color:#666;position:relative;white-space:nowrap;overflow:hidden}
.side li:last-child{border-bottom:none}
.side li::before{content:"";position:absolute;left:16px;top:12px;border-left:5px solid #777;border-top:4.5px solid transparent;border-bottom:4.5px solid transparent}

/* welcome */
.welcome-head{left:29px;top:501px;width:476px;height:39px;background:linear-gradient(90deg,var(--teal) 0%,var(--teal) 62%,var(--white) 100%);padding-left:17px;line-height:39px;font-family:"Roboto Condensed",sans-serif;font-weight:700;font-size:23px;color:var(--heading)}
.copy{left:29px;font-size:13.7px;line-height:20.6px;color:var(--text)}
.copy p{margin-bottom:20.6px}

/* video */
.video{left:520px;top:500px;width:380px;height:251px;background:var(--white);border:1px solid #d0d0d0;box-shadow:0 1px 4px rgba(0,0,0,.18)}
.video-frame{position:absolute;left:6px;top:6px;width:368px;height:210px;background:linear-gradient(135deg,#6b5a3e,#4a3a28 60%,#2c2218)}
.video-bar{position:absolute;left:6px;top:216px;width:368px;height:28px;background:linear-gradient(#3a3a3a,#111)}
.video-bar .time{position:absolute;left:72px;top:9px;font-size:9px;color:#ccc}

/* form */
.form{left:920px;top:768px;width:251px;height:270px;background:var(--panel);border:1px solid var(--panel-line)}
.field{position:absolute;left:17px;width:217px;height:26px;background:var(--field);border:1px solid #cfcfcf;padding:5px 7px;font-size:13.5px;color:#444}
.send{position:absolute;left:17px;top:226px;width:55px;height:25px;background:var(--teal);border:1px solid var(--teal-dark);font-size:13.5px;color:#222;text-align:center;line-height:23px;border-radius:2px}

/* footer */
.footer{left:29px;top:1055px;width:1142px;height:78px;background:var(--footer);font-size:12.5px;color:#444}
.footer .links{position:absolute;left:0;top:20px}
.footer .copyright{position:absolute;left:0;top:43px}
.footer .address{position:absolute;right:0;top:14px;display:flex;gap:8px;line-height:19px}
</style>
</head>
<body>

<header>
  <div class="abs topbar"></div>
  <nav class="abs nav">
    <a class="active" href="#">Home</a><a href="#">About Us</a><a href="#">Course</a><a href="#">Faculty</a><a href="#">Contact Us</a>
  </nav>
  <div class="abs contact-top">
    <span><svg width="22" height="18" viewBox="0 0 22 18"><path d="M1 6c0-4 20-4 20 0v2h-5V6c-2-1-8-1-10 0v2H1z M5 9h12l3 8H2z" fill="#333"/><circle cx="11" cy="13" r="2.2" fill="#eee"/></svg>+47 93516270</span>
    <span><svg width="22" height="17" viewBox="0 0 22 17"><path d="M1 7 11 1l10 6v9H1z" fill="#333"/><path d="M4 6h14v5l-7 3-7-3z" fill="#fff"/><path d="M1 8l10 6 10-6" stroke="#eee" fill="none"/></svg>info@kalirom.example</span>
  </div>
  <div class="abs brand"><i></i>Kali Rom</div>
</header>

<section class="abs slider">
  <div class="slide-photo" role="img" aria-label="Rotating banner photo of children seated at desks in a classroom with a teacher"></div>
  <svg class="arrow" style="left:10px" width="44" height="112" viewBox="0 0 44 112"><path d="M40 2 6 56l34 54" stroke="#fff" stroke-width="7" fill="none"/></svg>
  <svg class="arrow" style="left:820px" width="44" height="112" viewBox="0 0 44 112"><path d="M4 2l34 54-34 54" stroke="#fff" stroke-width="7" fill="none"/></svg>
  <div class="dots"><i class="on"></i><i></i><i></i><i></i><i></i></div>
</section>

<aside class="abs side" style="top:64px">
  <h3>Next available Course</h3>
  <ul>
    <li>Lorem Ipsum is simply dummy</li><li>Text of the printing and typeset-</li><li>Ting industry. Lorem Ipsum has</li><li>Been the industry's standard</li><li>Dummy text ever since the when</li><li>Unknown printer took a galley of</li><li>Type and scrambled it to make a</li><li>Type specimen book.</li><li>It has survived not only five</li><li>Centuries, but also the leap into</li><li>Electronic typesetting, remaining</li>
  </ul>
</aside>

<h2 class="abs welcome-head">Welcome to Kali Rom</h2>
<div class="abs copy" style="top:550px;width:470px">
  <p>Kali Rom is part of a global network of education institution committed to rht maintenance of the natural dentition. We teach endodontic and restoratice concepts, lectures and hands-on courses in Center City, Philadelphia, Penn-sylvania and throughout the world. At Crestline Endodontic, our goal is to help you, as a dentist, determine what level of endodontic knowledge and skill you currently possess and assist you currently your personal next level through one of our course offering.</p>
  <p>Kali Rom is part of a global network of education institution committed to rht maintenance of the natural dentition.</p>
</div>

<div class="abs video">
  <div class="video-frame" role="img" aria-label="Video still of students in a classroom"></div>
  <svg class="abs" style="left:163px;top:95px" width="44" height="44" viewBox="0 0 44 44"><circle cx="22" cy="22" r="21" fill="#333" fill-opacity=".75" stroke="#ddd" stroke-width="1.5"/><path d="M17 12l13 10-13 10z" fill="#eee"/></svg>
  <div class="video-bar">
    <svg class="abs" style="left:0;top:-6px" width="368" height="34" viewBox="0 0 368 34">
      <rect x="0" y="3" width="368" height="3" fill="#555"/><circle cx="6" cy="4.5" r="4" fill="#eee"/>
      <path d="M16 13l8 5-8 5z" fill="#aaa"/>
      <path d="M46 15h3l4-3v12l-4-3h-3z" fill="#aaa"/>
      <rect x="188" y="13" width="9" height="7" fill="#d33"/><rect x="208" y="13" width="9" height="8" fill="#aaa"/>
      <circle cx="234" cy="17" r="4" fill="#aaa"/><circle cx="254" cy="17" r="4" fill="#aaa"/>
      <rect x="272" y="14" width="10" height="6" stroke="#aaa" fill="none"/><rect x="290" y="13" width="12" height="8" stroke="#aaa" fill="none"/>
      <path d="M310 12h3m-3 0v3m12-3h-3m3 0v3m-12 7h3m-3 0v-3m12 3h-3m3 0v-3" stroke="#aaa"/>
    </svg>
    <span class="time">00:00 / 43:07</span>
  </div>
</div>

<div class="abs copy" style="top:777px;width:875px">
  <p>Kali Rom is part of a global network of education institution committed to rht maintenance of the natural dentition. We teach endodontic and restoratice concepts, lectures and hands-on courses in Center City, Philadelphia, Pennsylvania and throughout the world. At Crestline Endodontic, our goal is to help you, as a dentist, determine what level of endodontic knowledge and skill you currently possess and assist you currently your personal next level through one of our course offering.</p>
  <p>Kali Rom is part of a global network of education institution committed to rht maintenance of the natural dentition. We teach endodontic and restoratice concepts, lectures and hands-on courses in Center City.<br>&nbsp;Philadelphia, Pennsylvania and throughout the world. At Crestline Endodontic, our goal is to help you, as a dentist, determine what level of endodontic knowledge and skill you currently possess and assist you currently your personal next level through one of our course offering. Kali Rom is part of a global network of education institution committed to rht maintenance of the natural dentition. We teach endodontic and restoratice concepts, lectures and hands-on courses in Center City.</p>
</div>

<aside class="abs side" style="top:501px">
  <h3>Current courses available</h3>
  <ul>
    <li>Lorem Ipsum is simply dummy</li><li>Text of the printing and typeset-</li><li>Ting industry. Lorem Ipsum has</li><li>Been the industry's standard</li><li>Dummy text ever since the when</li><li>Unknown printer took a galley of</li>
  </ul>
</aside>

<aside class="abs side form">
  <h3>Contact Form</h3>
  <div class="field" style="top:54px">Name</div>
  <div class="field" style="top:88px">Email</div>
  <div class="field" style="top:122px">Phone</div>
  <div class="field" style="top:156px;height:60px">Massage</div>
  <div class="send">Send</div>
</aside>

<footer class="abs footer">
  <div class="links">Home &nbsp;| &nbsp;About Us &nbsp;| &nbsp;Course &nbsp;| &nbsp;Faculty &nbsp;| &nbsp;Contact Us &nbsp;| &nbsp;Sitemap</div>
  <div class="copyright">© 2012-2013 &nbsp;Kali Rom, All Rights reseved</div>
  <div class="address"><span>Address:</span><span>Lorem Ipsum is,<br>simply dummy,<br>25, street</span></div>
</footer>

</body>
</html>
```